Business card, Invoice and printable service brochure

I need a 5.5x8.5 invoice, business card and printable service template for reception desk designed for my Rug repair, restoration and cleaning business.

I have included a picture for reference

www.kolvenrug.com

Columns i need in my invoice:
Type of rug, Size, Background Color, Repair needs, Notes, Price and rug cleaning disclaimer.

Target Market(s)

Higher segment clients

Industry/Entity Type

Rug Repair, Restoration and cleaning,

Requirements
Must have
• Services hast to be listed on the invoice as well as service brochure.

```html
<!DOCTYPE html>
<html lang="en">
<head>
<meta charset="utf-8">
<title>Kolven Rug – Invoice and Business Card</title>
<link rel="stylesheet" href="https://fonts.googleapis.com/css2?family=Fira+Sans:wght@300;400;500;600;700&family=Fira+Sans+Condensed:wght@500;600;700&display=swap">
<style>
:root{
  --gold:#b3955e;
  --ink:#0b0b0b;
  --paper:#ffffff;
  --stage:#c6c8c7;
  --text:#1c1c1c;
  --light:#f2f2f2;
}
*{box-sizing:border-box;margin:0;padding:0}
html,body{width:1200px;height:1010px;overflow:hidden}
body{background:var(--stage);font-family:"Fira Sans",sans-serif;color:var(--text);position:relative}
.abs{position:absolute}
.piece-label{position:absolute;font-size:13.5px;color:#2a2a2a;font-weight:400}
svg.icons{position:absolute;width:0;height:0}
.ico{width:7px;height:7px;fill:var(--gold);vertical-align:-1px;margin-right:4px}

/* invoice */
.invoice{position:absolute;left:74px;top:105px;width:528px;height:815px;background:var(--paper);overflow:hidden}
.inv-brand{position:absolute;left:0;top:0;width:323px;height:146px;background:var(--ink);border-right:3px solid var(--gold);border-bottom:3px solid var(--gold)}
.inv-black-strip{position:absolute;left:323px;top:0;width:9px;height:151px;background:var(--ink)}
.brand-name{position:absolute;font-weight:300;color:var(--gold);white-space:nowrap;letter-spacing:.02em;line-height:1}
.brand-tag{position:absolute;color:var(--gold);white-space:nowrap;font-weight:500}
.inv-brand .brand-name{left:28px;top:18px;font-size:39px}
.inv-brand .brand-tag{left:28px;top:62px;font-size:8.6px;letter-spacing:.36em}
.inv-contact{position:absolute;left:27px;top:81px;color:#fff;font-size:9px;line-height:13px}
.inv-hours{position:absolute;left:205px;top:81px;color:#fff;font-size:9px;line-height:14px;border-left:1.5px solid var(--gold);padding-left:8px;height:48px}
.inv-hours b{font-weight:600}
.bill-to{position:absolute;left:332px;top:0;width:196px;height:146px;background:var(--gold);padding:44px 0 0 16px}
.bill-to h2{font-family:"Fira Sans Condensed",sans-serif;font-weight:700;font-size:17px;color:var(--ink);margin-bottom:6px}
.bill-to p{font-size:9px;color:#3a3020;line-height:19px}
.band-black{position:absolute;left:0;top:146px;width:528px;height:5px;background:var(--ink)}
.band-gold{position:absolute;left:0;top:151px;width:528px;height:5px;background:var(--gold)}
.meta-row{position:absolute;top:160px;font-size:9px}
.table-head{position:absolute;left:0;top:185px;width:528px;height:32px;background:var(--gold);font-family:"Fira Sans Condensed",sans-serif;font-weight:600;font-size:11px;color:#2b2417}
.table-head span{position:absolute;top:0;height:32px;line-height:32px;text-align:center}
.col-rule{position:absolute;width:1px;background:var(--gold)}
.table-head .col-rule{background:#fff;top:3px;height:26px}
.row-rule{position:absolute;left:17px;width:492px;height:1px;background:var(--gold)}
.pay-info{position:absolute;left:29px;top:581px;font-size:10px;line-height:16px}
.pay-info b{font-weight:600}
.totals{position:absolute;left:365px;top:581px;font-size:10px;font-weight:600;line-height:13px}
.total-box{position:absolute;left:356px;top:609px;width:151px;height:33px;background:var(--gold);font-size:10.5px;font-weight:600;padding:12px 0 0 9px}
.section-head{position:absolute;left:29px;font-weight:600;white-space:nowrap}
.section-head .rule{display:inline-block;height:1px;background:#333;vertical-align:2px;margin-left:5px}
.note{position:absolute;left:29px;top:663px;width:480px;font-size:7.6px;line-height:11px}
.note b{font-weight:600}
.disclaimer{position:absolute;left:29px;top:705px;width:481px;font-size:5.6px;line-height:8.6px;color:#222}
.services{position:absolute;left:0;top:748px;width:528px;height:67px;background:var(--ink);text-align:center}
.services h3{position:absolute;left:224px;top:1px;width:80px;height:18px;border:1.5px solid var(--gold);border-radius:9px;color:#fff;font-family:"Fira Sans Condensed",sans-serif;font-weight:600;font-size:13px;line-height:15px}
.service-line{position:absolute;left:0;width:528px;font-family:"Fira Sans Condensed",sans-serif;font-weight:600;font-size:10.5px;color:var(--gold);white-space:nowrap}
.service-line i{font-style:normal;color:#fff;margin:0 7px;font-weight:400}

/* business cards */
.card{position:absolute;width:341px;height:190px;overflow:hidden}
.card-front{left:734px;top:273px;background:var(--ink)}
.card-front .brand-name{left:0;width:341px;text-align:center;top:53px;font-size:28px}
.card-front .brand-tag{left:0;width:341px;text-align:center;top:86px;font-size:6.6px;letter-spacing:.32em}
.stripe{position:absolute;left:0;width:341px;background:var(--gold)}
.card-back{left:732px;top:538px;background:var(--paper)}
.holder{position:absolute;left:35px;top:23px;font-size:10px;line-height:11px}
.holder b{font-weight:600}
.holder small{display:block;font-size:8px}
.back-contact{position:absolute;left:35px;top:108px;font-size:7.4px;line-height:20px}
.back-divider{position:absolute;left:199px;top:113px;width:1px;height:77px;background:var(--gold)}
.card-back .brand-name{left:208px;top:113px;font-size:16px;color:var(--ink)}
.card-back .brand-tag{left:208px;top:131px;font-size:4.2px;letter-spacing:.3em;color:var(--ink)}
.back-hours{position:absolute;left:208px;top:145px;font-size:7.4px;line-height:11px}
</style>
</head>
<body>

<svg class="icons" aria-hidden="true">
  <symbol id="i-pin" viewBox="0 0 10 10"><path d="M5 0a3.5 3.5 0 0 0-3.5 3.5C1.5 6 5 10 5 10s3.5-4 3.5-6.5A3.5 3.5 0 0 0 5 0zm0 5a1.5 1.5 0 1 1 0-3 1.5 1.5 0 0 1 0 3z"/></symbol>
  <symbol id="i-phone" viewBox="0 0 10 10"><path d="M2 .5l2 2-1 1.2c.6 1.3 1.6 2.3 2.9 2.9L7 5.6l2.5 2-1 1.8C4.5 9.4.6 5.5.6 1.5z"/></symbol>
  <symbol id="i-mail" viewBox="0 0 10 10"><path d="M0 2h10v6.5H0zm1 1v.4l4 2.6 4-2.6V3z"/></symbol>
  <symbol id="i-web" viewBox="0 0 10 10"><path d="M5 0a5 5 0 1 0 0 10A5 5 0 0 0 5 0zm-.6 1.1v1.6H2.6A4 4 0 0 1 4.4 1.1zm1.2 0a4 4 0 0 1 1.8 1.6H5.6zM1.9 3.8h2.5v1.7H1.2a4 4 0 0 1 .7-1.7zm3.7 0h2.5a4 4 0 0 1 .7 1.7H5.6zM1.3 6.5h3.1v2.3A4 4 0 0 1 1.3 6.5zm4.3 0h3.1a4 4 0 0 1-3.1 2.3z"/></symbol>
</svg>

<p class="piece-label" style="left:73px;top:87px">Invoice front</p>
<p class="piece-label" style="left:733px;top:249px">business card front</p>
<p class="piece-label" style="left:731px;top:514px">business card back</p>

<section class="invoice" aria-label="Invoice front">
  <header class="inv-brand">
    <p class="brand-name">KOLVEN RUG</p>
    <p class="brand-tag">REPAIR | RESTORATION | CLEANING</p>
    <div class="inv-contact">
      <p><svg class="ico"><use href="#i-pin"/></svg>1482 Marlow Ave, Evanston, IL 60201</p>
      <p><svg class="ico"><use href="#i-phone"/></svg>(847)555-0193</p>
      <p><svg class="ico"><use href="#i-mail"/></svg>info@kolvenrug.com</p>
      <p><svg class="ico"><use href="#i-web"/></svg>www.kolvenrug.com</p>
    </div>
    <div class="inv-hours">
      <p>Monday - Friday 9AM–5PM</p>
      <p>Saturday 12PM–5PM</p>
      <p><b>SUNDAY CLOSED</b></p>
    </div>
  </header>
  <div class="inv-black-strip"></div>
  <div class="bill-to">
    <h2>Invoice to</h2>
    <p>Client Name</p>
    <p>Street Address Lane</p>
    <p>Client City</p>
    <p>Mobile</p>
  </div>
  <div class="band-black"></div>
  <div class="band-gold"></div>
  <p class="meta-row" style="left:41px">Date:</p>
  <p class="meta-row" style="left:348px">Invoice NO.</p>

  <div class="table-head">
    <span style="left:17px;width:136px;text-align:left;padding-left:24px">Type of Rug</span>
    <span style="left:153px;width:118px">Background Color</span>
    <span style="left:271px;width:68px">SIZE</span>
    <span style="left:339px;width:74px">PRICE</span>
    <span style="left:413px;width:105px">TOTAL</span>
    <i class="col-rule" style="left:153px"></i>
    <i class="col-rule" style="left:271px"></i>
    <i class="col-rule" style="left:339px"></i>
    <i class="col-rule" style="left:413px"></i>
  </div>
  <div class="table-body">
    <i class="col-rule" style="left:153px;top:222px;height:345px"></i>
    <i class="col-rule" style="left:271px;top:222px;height:345px"></i>
    <i class="col-rule" style="left:339px;top:222px;height:345px"></i>
    <i class="col-rule" style="left:413px;top:222px;height:345px"></i>
    <i class="row-rule" style="top:265px"></i>
    <i class="row-rule" style="top:316px"></i>
    <i class="row-rule" style="top:367px"></i>
    <i class="row-rule" style="top:418px"></i>
    <i class="row-rule" style="top:469px"></i>
    <i class="row-rule" style="top:520px"></i>
  </div>

  <div class="pay-info">
    <p><b>Payment Info:</b></p>
    <p>Account:</p>
    <p>Bank Detail:</p>
  </div>
  <div class="totals">
    <p>Sub Total:</p>
    <p>Tax</p>
  </div>
  <div class="total-box">Total</div>

  <p class="section-head" style="top:640px;font-size:10.5px">Repair Needs<span class="rule" style="width:243px"></span></p>
  <p class="note"><b>NOTE</b> that in some instances, cleaning/treatment of carpets (due to the sudden rise in humidity) can trigger the alarm on Carbon Monoxide Detectors. There is no need for concern</p>

  <p class="section-head" style="top:694px;font-size:6.6px;font-style:italic">RUG CLEANING DISCLAIMER.<span class="rule" style="width:213px"></span></p>
  <p class="disclaimer">Under our current policy, Kolven Rug is not liable for damage to carpets or upholstery beyond the area we are asked to treat. Every client receives this notice so that each point is covered in advance. Please note that carpets will remain damp for some time after cleaning, and extra care is needed when stepping from a damp area onto a tiled floor or vinyl surface, as these may become slippery. We ask clients to keep children and pets away from treated areas until fully dry, and to wear dry shoes indoors. Our team will explain drying times before leaving the home.</p>

  <footer class="services">
    <h3>SERVICES</h3>
    <p class="service-line" style="top:25px">STAIN REMOVAL<i>|</i>SHEARING<i>|</i>RUG CLEANING<i>|</i>RUG ALTERATION</p>
    <p class="service-line" style="top:42px">RUG BLOCKING AND STRETCHING<i>|</i>TEAR AND WEAR OR MAJOR RUG REPAIR<i>|</i>MOTH REMOVAL</p>
  </footer>
</section>

<section class="card card-front" aria-label="Business card front">
  <p class="brand-name">KOLVEN RUG</p>
  <p class="brand-tag">REPAIR | RESTORATION | CLEANING</p>
  <div class="stripe" style="top:141px;height:5px"></div>
  <div class="stripe" style="top:151px;height:5px"></div>
</section>

<section class="card card-back" aria-label="Business card back">
  <p class="holder"><b>DANIEL</b> REYES<small>Director</small></p>
  <div class="stripe" style="top:68px;height:6px"></div>
  <div class="stripe" style="top:74px;height:5px;background:var(--ink)"></div>
  <div class="stripe" style="top:79px;height:5px"></div>
  <div class="back-contact">
    <p><svg class="ico"><use href="#i-pin"/></svg>1482 Marlow Ave, Evanston, IL 60201</p>
    <p><svg class="ico"><use href="#i-phone"/></svg>(847)555-0193</p>
    <p><svg class="ico"><use href="#i-mail"/></svg>info@kolvenrug.com</p>
    <p><svg class="ico"><use href="#i-web"/></svg>www.kolvenrug.com</p>
  </div>
  <div class="back-divider"></div>
  <p class="brand-name">KOLVEN RUG</p>
  <p class="brand-tag">REPAIR | RESTORATION | CLEANING</p>
  <div class="back-hours">
    <p>Monday - Friday 9AM–5PM</p>
    <p>Saturday 12PM–5PM</p>
    <p>Sunday Closed</p>
  </div>
</section>

</body>
</html>
```